Web Design Project (Mente Lumo)

We are going to do a therapy template to a psychologist. The site already exists, adress: www.mentelumo.net. So, its a total redesign job. I'm from Brazil, the language is PT-BR, so I'm gonna translate what you think be necessary. You can use the current structure from the website as a base to the new design. Check this template to see what I usually like: http://www.layoutkiosk.example/demo/51937.html
Updates

I'm waiting for new creative designs. The 'structure' image is just for 'pb'.

Requirements
Must have
• We need a modern menu, it should use a cool font style and make some kind of effect and little noise when the user pass over with the mouse (FLASH/HTML 5). The main page must emphasize the fact that we offer online treatment, like a picture or frame saying "Online Treatment, click here". It must also show the therapist picture and her name. The colors need to pass a tranquility feeling. The clinic telephone must always be present, doesn't matter which page the user is. The website must adapt to any resolution above 1024x768, crossbrowsing and accept javascript (I'll use www.agendrix.example, so its necessary embed code)
Nice to have
• I would appreciate if there was some kind of slow background animation, passing behind the text using the transparency.
Should not have
• Can't take too long to load, and won't have news or blog

```html
<!DOCTYPE html>
<html lang="pt-BR">
<head>
<meta charset="utf-8">
<title>Mente Lumo</title>
<link href="https://fonts.googleapis.com/css2?family=Source+Sans+3:wght@300;400;600&display=swap" rel="stylesheet">
<style>
:root{
  --ink:#1a1a1a;
  --teal:#1f6f78;
  --teal-deep:#1d4f5a;
  --aqua:#4cc5d6;
  --aqua-dark:#2fa9bd;
  --sky:#dff6fb;
  --line:#d8d8d8;
  --black:#000;
}
*{margin:0;padding:0;box-sizing:border-box}
html,body{width:1200px;height:1135px;overflow:hidden}
body{position:relative;font-family:"Source Sans 3",sans-serif;color:var(--ink);
  background:linear-gradient(#cdeff6 130px,#f4fcfe 420px,#fff 700px,#fff 980px,#e3f6fb 1135px)}
.abs{position:absolute}
h1,h2,h3{font-weight:400}
.masthead{left:0;top:0;width:1200px;height:98px;background:var(--black);border-top:3px solid #333}
.brand{left:152px;top:22px;display:flex;align-items:center;gap:10px}
.brand-dot{width:46px;height:46px;border-radius:50%;background:#6fb6c4}
.brand-name{font-size:30px;font-weight:600;color:#cfe9d9}
.search{left:906px;top:25px;width:140px;height:38px;background:#fff;border:3px solid #bdbdbd;border-radius:3px}
.search svg{position:absolute;left:8px;top:8px}
.search-btn{position:absolute;right:6px;top:6px;height:20px;padding:0 5px;background:var(--aqua-dark);color:#fff;font-size:12px;line-height:20px}
.nav{left:0;top:98px;width:1200px;height:29px;background:linear-gradient(#7fd7e4,#47bdd0);border-bottom:1px solid #3aa8bb}
.nav ul{list-style:none;position:absolute;left:147px;top:0;display:flex;height:29px}
.nav li{font-size:12px;line-height:29px;text-align:center;color:#153b42;border-right:1px solid #37a7b9}
.nav li:last-child{border-right:0}
.panel{left:147px;top:137px;width:901px;height:838px;background:#fff;border:1px solid #dcdcdc;box-shadow:0 0 4px rgba(0,0,0,.05)}
.hero-shadow{left:90px;top:410px;width:1020px;height:16px;border-radius:50%;box-shadow:0 6px 10px rgba(0,0,0,.12)}
.hero-divider{left:147px;top:417px;width:901px;height:1px;background:#e6e6e6}
.hero-title{left:196px;top:188px;font-size:29px;line-height:37px;font-weight:300;color:var(--teal-deep)}
.hero-btn{left:197px;top:319px;width:145px;height:33px;border-radius:3px;background:linear-gradient(#6fd4e2,var(--aqua-dark));color:#fff;font-size:13px;font-weight:300;line-height:33px;padding-left:9px}
.hero-btn svg{position:absolute;right:10px;top:10px}
.hero-photo{left:450px;top:150px;width:565px;height:272px;background:radial-gradient(ellipse at 50% 55%,#e9eef2 0%,#f4f7f9 55%,rgba(255,255,255,0) 75%)}
.section-head{height:32px;width:310px;background:linear-gradient(90deg,#e9ecee,rgba(255,255,255,0));font-size:16px;font-weight:400;line-height:32px;color:var(--teal);padding-left:10px}
.portrait{left:165px;top:474px;width:126px;height:134px;background:linear-gradient(#8a8a8a,#4d4d4d)}
.welcome-text{left:306px;top:472px;width:433px;font-size:11.5px;line-height:19.4px;text-align:justify}
.welcome-text p+p{margin-top:9px}
.treat-box{left:166px;top:679px;width:572px;height:280px;border:1px solid #dcdcdc}
.treat-text{left:183px;top:693px;width:377px;font-size:11.5px;line-height:22px;text-align:justify}
.clipboard{left:580px;top:690px;width:143px;height:166px;background:linear-gradient(135deg,#4d9be0,#2a6fc2);border-radius:4px}
.treat-list{left:166px;top:870px;width:572px;text-align:center;font-size:13.5px;line-height:26px;color:var(--teal)}
.card{left:791px;width:234px;height:78px;border:1px solid #dedede;background:linear-gradient(#fff,#eaeaea);box-shadow:0 4px 4px -2px rgba(0,0,0,.25)}
.card h3{position:absolute;left:14px;top:17px;font-size:18px;font-weight:400;color:var(--teal)}
.card .more{position:absolute;left:16px;top:45px;font-size:11.5px;color:#222;display:flex;align-items:center;gap:5px}
.card-art{position:absolute;right:6px;bottom:0;width:64px;height:84px;background:linear-gradient(#e4e4e4,#c9c9c9);border-radius:4px 4px 0 0}
.loc-head{left:790px;top:783px;font-size:16px;font-weight:400;color:var(--teal)}
.map{left:790px;top:810px;width:242px;height:146px;background:linear-gradient(135deg,#efe6cf,#e6dcc0 50%,#ece4cb);border:1px solid #ccc}
.address{left:147px;top:993px;font-size:10px;line-height:19px;font-style:normal}
.phones{left:793px;top:1002px;display:flex;align-items:center;gap:8px;font-size:10px}
.rule{left:147px;top:1047px;width:897px;height:1px;background:#dadada}
.foot-nav{left:0;top:1067px;width:1200px;text-align:center;font-size:10px}
.foot-nav span{margin:0 5px}
.copyright{left:0;top:1087px;width:1200px;text-align:center;font-size:10px}
</style>
</head>
<body>
<header class="abs masthead"></header>
<div class="abs brand"><span class="brand-dot"></span><span class="brand-name">Mente Lumo</span></div>
<div class="abs search">
  <svg width="16" height="16" viewBox="0 0 16 16"><circle cx="6" cy="6" r="4.5" fill="none" stroke="#999" stroke-width="1.6"/><line x1="9.5" y1="9.5" x2="14" y2="14" stroke="#999" stroke-width="2"/></svg>
  <span class="search-btn">SEARCH</span>
</div>
<nav class="abs nav"><ul>
  <li style="width:120px">Home</li><li style="width:120px">Online Service</li><li style="width:121px">Treatments</li><li style="width:120px">Questions</li><li style="width:136px">Ask the expert</li><li style="width:136px">Location</li><li style="width:148px">Contact Us</li>
</ul></nav>

<div class="abs panel"></div>
<div class="abs hero-shadow"></div>
<div class="abs hero-divider"></div>
<h1 class="abs hero-title">SERVING YOUR<br>HEALTH<br>WITH EXCELLENCE</h1>
<div class="abs hero-btn">CLICK HERE MORE
  <svg width="13" height="13" viewBox="0 0 13 13"><circle cx="6.5" cy="6.5" r="6" fill="#fff"/><path d="M5 3.5l3.5 3-3.5 3z" fill="var(--aqua-dark)"/></svg>
</div>
<div class="abs hero-photo" role="img" aria-label="Group of smiling doctors in white coats"></div>

<h2 class="abs section-head" style="left:165px;top:431px">WELCOME TO MENTE LUMO</h2>
<div class="abs portrait" role="img" aria-label="Black and white portrait of the therapist"></div>
<div class="abs welcome-text">
  <p>A Terapia Cognitiva tem como método a interpretação de processos e conteúdos mentais (as cognições), e sua influência na vida cotidiana. O comportamento e a emoção vêm depois do processamento cognitivo. É vital conhecermos nossos pensamentos para termos controle sobre eles, e assim podemos: nutri-los, expandi-los, reduzi-los ou rejeitá-los.</p>
  <p>Todo distúrbio psíquico tem origem no pensamento. A Terapia Cognitiva educa através da busca de seu equilibrio emocional.</p>
</div>

<h2 class="abs section-head" style="left:165px;top:639px">TREATMENTS</h2>
<div class="abs treat-box"></div>
<p class="abs treat-text">Nos dias de hoje, todas as pessoas estão sujeitas a sofrer de algum disturbio psicológico. Isso acontece devido as pressões diárias que se não bem administradas, podem levar a diversas crises, afetando a vida pessoal, familiar e profissional. Realizo atendimentos para crianças, jovens, adultos, idosos e casais. Abaixo, você pode obter mais detalhes de algumas das mais comuns disfunções cogntivas:</p>
<div class="abs clipboard" role="img" aria-label="Clipboard with a stethoscope"></div>
<div class="abs treat-list">
  Depressão,&nbsp; Estresse,&nbsp; Ansiedade,&nbsp; Timidez,&nbsp; Agressividade,&nbsp; Ciúme,&nbsp; Assédio Sexual<br>
  Violência Doméstica,&nbsp; Transtorno de Humor,&nbsp; Transtorno Bipolar,&nbsp; Pânico,&nbsp; TOC<br>
  Fobia,&nbsp; Bulimia,&nbsp; Anorexia
</div>

<div class="abs card" style="top:462px">
  <div class="card-art" role="img" aria-label="Support attendant with headset" style="height:100px"></div>
  <h3>ONLINE SERVICES</h3>
  <span class="more">READ MORE <svg width="11" height="11" viewBox="0 0 11 11"><circle cx="5.5" cy="5.5" r="5" fill="#fff" stroke="#999"/><path d="M4.3 3l3 2.5-3 2.5z" fill="#777"/></svg></span>
</div>
<div class="abs card" style="top:584px">
  <div class="card-art" role="img" aria-label="Person holding a question mark sign" style="height:100px"></div>
  <h3>QUESTIONS</h3>
  <span class="more">READ MORE <svg width="11" height="11" viewBox="0 0 11 11"><circle cx="5.5" cy="5.5" r="5" fill="#fff" stroke="#999"/><path d="M4.3 3l3 2.5-3 2.5z" fill="#777"/></svg></span>
</div>
<div class="abs card" style="top:681px">
  <div class="card-art" role="img" aria-label="Telephone with email envelope" style="height:60px;bottom:12px"></div>
  <h3>CONTACT US</h3>
  <span class="more">READ MORE <svg width="11" height="11" viewBox="0 0 11 11"><circle cx="5.5" cy="5.5" r="5" fill="#fff" stroke="#999"/><path d="M4.3 3l3 2.5-3 2.5z" fill="#777"/></svg></span>
</div>

<h2 class="abs loc-head">LOCATION</h2>
<div class="abs map" role="img" aria-label="Street map showing the clinic location"></div>

<address class="abs address">Rua das Palmeiras, 145, 4th floor, room 12 - Center - Vila Serena, SP<br>contato@mentelumo.net</address>
<div class="abs phones">
  <svg width="16" height="20" viewBox="0 0 16 20"><path d="M4 1l3 4-2 2c1 3 3 6 6 8l2-2 3 3-2 3C7 18 1 10 1 3z" fill="#111"/></svg>
  <span>(11) 3555-0142 &nbsp;&nbsp;|&nbsp;&nbsp; (11) 9555-0173 &nbsp;&nbsp;|&nbsp;&nbsp; (11) 7555-0198</span>
</div>
<div class="abs rule"></div>
<div class="abs foot-nav"><span>Home</span>|<span>Online Service</span>|<span>Treatments</span>|<span>Questions</span>|<span>Ask the expert</span>|<span>Location</span>|<span>Contact</span></div>
<div class="abs copyright">© Copyright 2012 - All rights reserved</div>
</body>
</html>
```